KV PowerPoint Design

I need a slick PowerPoint template following my newly designed logo (see the attached ZIP file for logo details, fonts, and colors).
Please also see the Sample.pptx file for an idea of the simplicity and slickness I am after (do not consider the colors or fonts from the Sample file, just as an idea). Other ideas are very welcome.

```html
<!DOCTYPE html>
<html lang="en">
<head>
<meta charset="utf-8">
<title>KV PowerPoint Template</title>
<link href="https://fonts.googleapis.com/css2?family=Poppins:ital,wght@0,400;0,500;0,600;0,700;0,800;1,500&family=Oswald:wght@600&display=swap" rel="stylesheet">
<style>
:root{
  --navy:#12187a;
  --royal:#2233b0;
  --blue:#2d45c8;
  --ink:#1b1d3a;
  --muted:#8c90a8;
  --grey:#b7b9c4;
  --paper:#ffffff;
  --board:#e3e4e8;
  --grad:linear-gradient(135deg,#2d45c8 0%,#12187a 100%);
}
*{box-sizing:border-box;margin:0;padding:0}
html,body{width:786px;height:1200px;overflow:hidden}
body{background:var(--board);font-family:'Poppins',sans-serif;color:var(--ink);position:relative}
.slide{position:absolute;width:228px;height:128px;background:var(--paper);overflow:hidden;box-shadow:0 1px 3px rgba(0,0,0,.18)}
.abs{position:absolute}
.badge{position:absolute;top:5px;right:6px;width:12px;height:12px;border-radius:50%;border:1px solid var(--navy);font-size:4.4px;font-weight:700;color:var(--navy);display:flex;align-items:center;justify-content:center}
.foot{position:absolute;left:16px;right:8px;bottom:7px;height:.6px;background:var(--royal)}
.foot-mark{position:absolute;left:5px;bottom:4px;font-size:4px;font-weight:700;color:var(--navy)}
.foot-url{position:absolute;left:14px;bottom:4.5px;font-size:1.8px;color:var(--muted)}
.page{position:absolute;right:6px;bottom:2px;font-size:2.4px;color:var(--ink)}
.title{font-weight:700;color:var(--navy);font-size:7.5px;line-height:1.1}
.rule{display:block;width:12px;height:1px;background:var(--royal);margin-top:3px}
.tx{font-size:2.5px;line-height:1.35;color:var(--muted)}
.tx-w{font-size:2.5px;line-height:1.35;color:#dfe3ff}
.sub{font-size:3.6px;font-weight:600;color:var(--royal)}
.photo{position:absolute;background:linear-gradient(135deg,#c9ccd8,#6b7086 60%,#2b2f56)}
.photo-warm{position:absolute;background:linear-gradient(135deg,#e3ddd2,#9a8f82 55%,#4a4a5e)}
.photo-sky{position:absolute;background:linear-gradient(160deg,#e6edf6,#a9b6cc 55%,#1f2333)}
.block{position:absolute;background:var(--grad)}
.icon-dot{position:absolute;width:11px;height:11px;border-radius:50%;background:var(--royal);border:1.2px solid #fff;box-shadow:0 0 0 1px var(--royal)}
.list-num{font-weight:700;color:var(--navy);font-size:3.6px}
.member{width:44px;text-align:center}
.member-photo{width:18px;height:18px;border-radius:50%;margin:0 auto;background:linear-gradient(135deg,#dcd7cf,#8d8a93);border:1.2px solid #fff}
.member-name{font-size:3.6px;font-weight:700;margin-top:3px}
</style>
</head>
<body>

<!-- Row 1 -->
<section class="slide" style="left:40px;top:38px;background:var(--grad)">
  <div class="abs" style="left:10px;top:12px;width:22px;height:22px;border-radius:50%;border:1.2px solid #c9cde8;color:#fff;font-size:8px;font-weight:700;display:flex;align-items:center;justify-content:center">KV</div>
  <div class="abs" style="right:6px;top:30px;font-size:70px;font-weight:800;color:rgba(255,255,255,.18);line-height:1">KV</div>
  <div class="abs" style="left:15px;top:74px;color:#fff">
    <div style="font-size:8px;line-height:1">Company</div>
    <div style="font-size:14px;font-weight:700;line-height:1.05">Business</div>
    <div style="font-size:10px;line-height:1">Marketing</div>
  </div>
</section>

<section class="slide" style="left:282px;top:38px">
  <div class="abs" style="left:5px;top:5px;width:5px;height:5px;background:var(--navy)"></div>
  <div class="abs" style="left:24px;top:14px;width:20px;height:20px;border-radius:50%;border:1.2px solid var(--navy);font-size:7px;font-weight:700;color:var(--navy);display:flex;align-items:center;justify-content:center">KV</div>
  <div class="abs" style="left:13px;top:56px">
    <div style="font-family:'Oswald',sans-serif;font-weight:600;font-size:16px;color:var(--navy);line-height:1">BUSINESS</div>
    <div style="font-size:7px;font-weight:500;color:var(--navy);line-height:1.2">MARKETING</div>
    <div style="font-size:5px;font-style:italic;font-weight:500;margin-top:5px">Presentation</div>
    <div class="tx" style="width:60px;color:#4a4e6a">A short line to set the deck topic here.</div>
    <div style="font-size:6px;color:var(--navy);letter-spacing:1px;margin-top:3px;font-weight:700">•••</div>
  </div>
  <div class="photo" role="img" aria-label="Photo of a team working at computers in an office" style="left:96px;top:0;width:132px;height:108px"></div>
  <div class="block" style="left:96px;top:108px;width:132px;height:20px;display:flex;align-items:center;justify-content:center;color:#fff;font-size:4.4px;letter-spacing:1.3px">WWW.WEBSITE.COM</div>
</section>

<section class="slide" style="left:523px;top:38px">
  <div class="badge">KV</div>
  <div class="photo" role="img" aria-label="Photo of colleagues talking in a bright office" style="left:35px;top:11px;width:78px;height:104px"></div>
  <div class="abs" style="left:26px;top:32px;width:16px;height:63px;background:var(--navy);display:flex;align-items:center;justify-content:center"><span style="transform:rotate(90deg);color:#fff;font-weight:700;font-size:7px;white-space:nowrap">Agenda</span></div>
  <div class="abs" style="left:120px;top:26px;width:90px">
    <div class="sub">1. Lorem ipsum</div><div class="tx" style="margin:1px 0 6px 5px">A short note about the first agenda point here.</div>
    <div class="sub">2. Lorem ipsum</div><div class="tx" style="margin:1px 0 6px 5px">A short note about the second agenda point here.</div>
    <div class="sub">3. Lorem ipsum</div><div class="tx" style="margin:1px 0 6px 5px">A short note about the third agenda point here.</div>
    <div class="sub">4. Lorem ipsum</div><div class="tx" style="margin:1px 0 0 5px">A short note about the fourth agenda point here.</div>
  </div>
  <div class="foot"></div><div class="foot-mark">KV</div><div class="foot-url">www.website.com</div><div class="page">2</div>
</section>

<!-- Row 2 -->
<section class="slide" style="left:40px;top:180px">
  <div class="badge">KV</div>
  <div class="abs" style="left:0;top:35px;width:7px;height:62px;background:var(--navy)"></div>
  <div class="abs" style="left:13px;top:40px;font-weight:700;font-size:13px;line-height:1.12;color:var(--royal)">Text<br>Added<br>Here</div>
  <div class="photo-warm" role="img" aria-label="Photo of students studying with an education chalk drawing" style="left:72px;top:20px;width:156px;height:62px"></div>
  <div class="abs" style="left:100px;top:60px;width:46px;height:57px;background:#fff;box-shadow:0 1px 2px rgba(0,0,0,.15)">
    <div style="background:var(--royal);color:#fff;font-size:6px;font-weight:600;text-align:center;padding:2px 0">Text Here</div>
    <div class="tx" style="padding:3px 4px">Short supporting copy for this card. Keep it brief and clear for readers.</div>
  </div>
  <div class="abs" style="left:156px;top:60px;width:46px;height:57px;background:#fff;box-shadow:0 1px 2px rgba(0,0,0,.15)">
    <div style="background:var(--royal);color:#fff;font-size:6px;font-weight:600;text-align:center;padding:2px 0">Text Here</div>
    <div class="tx" style="padding:3px 4px">Short supporting copy for this card. Keep it brief and clear for readers.</div>
  </div>
  <div class="foot"></div><div class="foot-mark">KV</div><div class="foot-url">www.website.com</div><div class="page">3</div>
</section>

<section class="slide" style="left:282px;top:180px">
  <div class="badge">KV</div>
  <div class="abs" style="left:0;top:40px;width:4px;height:60px;background:var(--navy)"></div>
  <div class="abs" style="left:21px;top:44px;width:72px">
    <div class="title" style="font-size:10.5px;color:var(--ink)">Part One</div>
    <div class="tx" style="margin-top:3px">A short intro line for this part of the deck goes right here for now.</div>
    <div class="tx" style="margin-top:3px">One more short line with a little extra detail for this part.</div>
  </div>
  <div class="photo" role="img" aria-label="Photo of two business people reviewing a tablet" style="left:138px;top:18px;width:60px;height:92px"></div>
  <div class="block" style="left:101px;top:42px;width:38px;height:44px;display:flex;align-items:center;justify-content:center;color:#fff;font-family:'Oswald',sans-serif;font-size:24px">01</div>
  <div class="foot"></div><div class="foot-mark">KV</div><div class="foot-url">www.website.com</div><div class="page">4</div>
</section>

<section class="slide" style="left:523px;top:180px">
  <div class="badge">KV</div>
  <div class="block" style="left:95px;top:0;width:58px;height:22px"></div>
  <div class="photo-sky" role="img" aria-label="Photo of graduates raising caps against the sky" style="left:105px;top:22px;width:103px;height:81px"></div>
  <div class="abs" style="left:16px;top:25px;width:78px">
    <div class="title" style="font-size:7.5px;color:var(--navy)">Lorem Ipsum<br>Dolor Sit<br>Ametkeeper.</div>
    <span class="rule"></span>
    <div class="tx" style="margin-top:4px">A short paragraph for this slide with a few plain words to fill the space well and keep it tidy.</div>
    <div class="tx" style="margin-top:4px">One more brief line that adds a small extra detail here.</div>
  </div>
  <div class="foot"></div><div class="foot-mark">KV</div><div class="foot-url">www.website.com</div><div class="page">5</div>
</section>

<!-- Row 3 -->
<section class="slide" style="left:40px;top:322px">
  <div class="badge">KV</div>
  <div class="abs" style="left:10px;top:8px"><div class="title">Text Added Hare</div><span class="rule"></span></div>
  <div class="abs" style="left:26px;top:31px;width:96px">
    <div class="list-num">01. <span style="color:var(--royal)">Aliquam Erat Volutpat</span></div><div class="tx" style="margin:0 0 6px 6px">A short note on this first point.</div>
    <div class="list-num">02. <span style="color:var(--royal)">Consectetuer Adipiscing Elit</span></div><div class="tx" style="margin:0 0 6px 6px">A short note on this second point.</div>
    <div class="list-num">03. <span style="color:var(--royal)">Duis Autem Vel Eum</span></div><div class="tx" style="margin:0 0 6px 6px">A short note on this third point.</div>
    <div class="list-num">04. <span style="color:var(--royal)">Aliquam Erat Volutpat</span></div><div class="tx" style="margin:0 0 0 6px">A short note on this fourth point.</div>
  </div>
  <div class="block" style="left:125px;top:28px;width:79px;height:80px"></div>
  <div class="icon-dot" style="left:119px;top:36px"></div>
  <div class="icon-dot" style="left:119px;top:61px"></div>
  <div class="icon-dot" style="left:119px;top:85px"></div>
  <div class="abs" style="left:138px;top:36px;width:62px;color:#fff">
    <div style="font-size:4px;font-weight:600">Lorem ipsum</div><div class="tx-w" style="margin-bottom:8px">Short copy for this item here.</div>
    <div style="font-size:4px;font-weight:600">Lorem ipsum</div><div class="tx-w" style="margin-bottom:8px">Short copy for this item here.</div>
    <div style="font-size:4px;font-weight:600">Lorem ipsum</div><div class="tx-w">Short copy for this item here.</div>
  </div>
  <div class="foot"></div><div class="foot-mark">KV</div><div class="foot-url">www.website.com</div><div class="page">6</div>
</section>

<section class="slide" style="left:282px;top:322px">
  <div class="badge">KV</div>
  <div class="abs" style="left:0;top:12px;width:3px;height:36px;background:var(--navy)"></div>
  <div class="abs" style="left:12px;top:13px;width:86px">
    <div class="title" style="font-size:9.5px;color:var(--ink);line-height:1.2">Lorem<br>Dolor Sit<br>Consectetuer</div>
    <div class="tx" style="margin-top:3px">A short paragraph that gives context to the numbers shown at right.</div>
  </div>
  <div class="abs" style="left:124px;top:27px;width:40px;text-align:center"><div style="font-size:7.5px;font-weight:700">768K</div><div style="font-size:4px;font-weight:600;color:var(--royal)">Lorem Ipsum</div><div class="tx">Brief stat note.</div></div>
  <div class="abs" style="left:172px;top:27px;width:40px;text-align:center"><div style="font-size:7.5px;font-weight:700">423K</div><div style="font-size:4px;font-weight:600;color:var(--royal)">Lorem Ipsum</div><div class="tx">Brief stat note.</div></div>
  <div class="block" style="left:106px;top:58px;width:122px;height:14px;display:flex;align-items:center;justify-content:center;color:#fff;font-size:7px;font-weight:600">Text Added Here</div>
  <div class="abs" style="left:51px;top:72px;width:4px;height:44px;background:var(--navy)"></div>
  <div class="photo-warm" role="img" aria-label="Photo of a team meeting around a presentation board" style="left:55px;top:72px;width:160px;height:44px"></div>
  <div class="foot"></div><div class="foot-mark">KV</div><div class="foot-url">www.website.com</div><div class="page">7</div>
</section>

<section class="slide" style="left:523px;top:322px">
  <div class="badge">KV</div>
  <div class="abs" style="left:10px;top:10px"><div class="title">Text Added Hare</div><span class="rule"></span></div>
  <div class="abs" style="left:16px;top:44px;width:58px"><div class="sub" style="font-size:3.4px"><span style="color:var(--navy)">01.</span> Project Problem</div><div class="tx">Short note on this point here.</div></div>
  <div class="abs" style="left:77px;top:44px;width:58px"><div class="sub" style="font-size:3.4px"><span style="color:var(--navy)">02.</span> Project Solution</div><div class="tx">Short note on this point here.</div></div>
  <div class="abs" style="left:16px;top:75px;width:58px"><div class="sub" style="font-size:3.4px"><span style="color:var(--navy)">03.</span> Project Problem</div><div class="tx">Short note on this point here.</div></div>
  <div class="abs" style="left:77px;top:75px;width:58px"><div class="sub" style="font-size:3.4px"><span style="color:var(--navy)">04.</span> Project Solution</div><div class="tx">Short note on this point here.</div></div>
  <div class="abs" style="left:138px;top:34px;width:36px;height:35px;background:var(--navy);color:#fff;padding:16px 4px 0"><div style="font-size:3.6px;font-weight:700">PROBLEM</div><div class="tx-w">Brief tile note.</div></div>
  <div class="abs" style="left:176px;top:34px;width:36px;height:35px;background:var(--royal);color:#fff;padding:16px 4px 0"><div style="font-size:3.6px;font-weight:700">SOLUTION</div><div class="tx-w">Brief tile note.</div></div>
  <div class="abs" style="left:138px;top:71px;width:36px;height:35px;background:var(--royal);color:#fff;padding:14px 4px 0"><div style="font-size:3.6px;font-weight:700">MARKET</div><div class="tx-w">Brief tile note.</div></div>
  <div class="abs" style="left:176px;top:71px;width:36px;height:35px;background:var(--navy);color:#fff;padding:14px 4px 0"><div style="font-size:3.6px;font-weight:700">MISSION</div><div class="tx-w">Brief tile note.</div></div>
  <div class="foot"></div><div class="foot-mark">KV</div><div class="foot-url">www.website.com</div><div class="page">8</div>
</section>

<!-- Row 4 -->
<section class="slide" style="left:40px;top:464px">
  <div class="badge">KV</div>
  <div class="abs" style="left:12px;top:11px"><div class="title" style="color:var(--ink)">Text<br>Added Hare</div><span class="rule"></span></div>
  <div class="block" style="left:0;top:42px;width:73px;height:63px"></div>
  <div class="abs" style="left:12px;top:47px;width:58px;color:#fff">
    <div style="display:flex;gap:3px;margin-bottom:5px"><span style="background:#fff;color:var(--navy);font-size:4px;font-weight:700;padding:0 2px;height:6px">1.</span><div><div style="font-size:3.4px;font-weight:600">Lorem ipsum</div><div class="tx-w">Short note on this item.</div></div></div>
    <div style="display:flex;gap:3px;margin-bottom:5px"><span style="background:#fff;color:var(--navy);font-size:4px;font-weight:700;padding:0 2px;height:6px">2.</span><div><div style="font-size:3.4px;font-weight:600">Lorem ipsum</div><div class="tx-w">Short note on this item.</div></div></div>
    <div style="display:flex;gap:3px"><span style="background:#fff;color:var(--navy);font-size:4px;font-weight:700;padding:0 2px;height:6px">3.</span><div><div style="font-size:3.4px;font-weight:600">Lorem ipsum</div><div class="tx-w">Short note on this item.</div></div></div>
  </div>
  <svg class="abs" style="left:80px;top:26px" width="140" height="96" viewBox="0 0 140 96" font-family="Poppins,sans-serif" font-size="3" fill="#555">
    <line x1="0" y1="70" x2="138" y2="70" stroke="#ccc" stroke-width=".4"/>
    <g><rect x="7" y="12" width="3" height="58" fill="#12187a"/><rect x="14" y="38" width="3" height="32" fill="#2d45c8"/><rect x="21" y="43" width="3" height="27" fill="#b7b9c4"/>
    <text x="5" y="10">43%</text><text x="12" y="36">24%</text><text x="20" y="41">20%</text><text x="14" y="76">1</text></g>
    <g><rect x="40" y="11" width="3" height="59" fill="#12187a"/><rect x="47" y="37" width="3" height="33" fill="#2d45c8"/><rect x="54" y="43" width="3" height="27" fill="#b7b9c4"/>
    <text x="38" y="9">44%</text><text x="45" y="35">25%</text><text x="52" y="41">20%</text><text x="47" y="76">2</text></g>
    <g><rect x="74" y="23" width="3" height="47" fill="#12187a"/><rect x="81" y="46" width="3" height="24" fill="#2d45c8"/><rect x="88" y="30" width="3" height="40" fill="#b7b9c4"/>
    <text x="72" y="21">35%</text><text x="80" y="44">18%</text><text x="87" y="28">30%</text><text x="81" y="76">3</text></g>
    <g><rect x="107" y="10" width="3" height="60" fill="#12187a"/><rect x="114" y="33" width="3" height="37" fill="#2d45c8"/><rect x="121" y="4" width="3" height="66" fill="#b7b9c4"/>
    <text x="105" y="8">45%</text><text x="113" y="31">28%</text><text x="120" y="2.5">50%</text><text x="114" y="76">4</text></g>
    <rect x="44" y="83" width="2" height="2" fill="#12187a"/><text x="47" y="85">Series1</text>
    <rect x="58" y="83" width="2" height="2" fill="#2d45c8"/><text x="61" y="85">Series2</text>
    <rect x="72" y="83" width="2" height="2" fill="#b7b9c4"/><text x="75" y="85">Series3</text>
  </svg>
  <div class="foot"></div><div class="foot-mark">KV</div><div class="foot-url">www.website.com</div><div class="page">9</div>
</section>

<section class="slide" style="left:282px;top:464px">
  <div class="badge">KV</div>
  <div class="abs" style="left:0;top:36px;width:4px;height:60px;background:var(--navy)"></div>
  <div class="abs" style="left:0;right:0;top:11px;text-align:center"><div class="title" style="color:var(--ink)">Text Added Hare</div><span class="rule" style="margin:3px auto 0"></span></div>
  <div class="tx abs" style="left:44px;right:44px;top:29px;text-align:center">A short centred paragraph introducing the three key percentages shown below for this section of the deck.</div>
  <svg class="abs" style="left:28px;top:52px" width="172" height="40" viewBox="0 0 172 40" font-family="Poppins,sans-serif" font-weight="600" font-size="9" text-anchor="middle" fill="#1b1d3a">
    <g transform="translate(27,20)"><circle r="15" fill="none" stroke="#e4e5ea" stroke-width="2.5"/><circle r="15" fill="none" stroke="#12187a" stroke-width="2.5" stroke-dasharray="47.1 94.2" transform="rotate(-90)"/><text y="3">50%</text></g>
    <g transform="translate(86,20)"><circle r="15" fill="none" stroke="#e4e5ea" stroke-width="2.5"/><circle r="15" fill="none" stroke="#2d45c8" stroke-width="2.5" stroke-dasharray="70.7 94.2" transform="rotate(-90)"/><text y="3">75%</text></g>
    <g transform="translate(145,20)"><circle r="15" fill="none" stroke="#e4e5ea" stroke-width="2.5"/><circle r="15" fill="none" stroke="#b7b9c4" stroke-width="2.5" stroke-dasharray="37.7 94.2" transform="rotate(-90)"/><text y="3">40%</text></g>
  </svg>
  <div class="tx abs" style="left:30px;top:100px;width:52px;text-align:center">Short caption for this value.</div>
  <div class="tx abs" style="left:88px;top:100px;width:52px;text-align:center">Short caption for this value.</div>
  <div class="tx abs" style="left:147px;top:100px;width:52px;text-align:center">Short caption for this value.</div>
  <div class="foot"></div><div class="foot-mark">KV</div><div class="foot-url">www.website.com</div><div class="page">9</div>
</section>

<section class="slide" style="left:523px;top:464px">
  <div class="badge">KV</div>
  <div class="abs" style="left:12px;top:10px;width:70px"><div class="title" style="color:var(--ink)">Text<br>Added Hare</div><span class="rule"></span>
    <div class="tx" style="margin-top:4px">A short paragraph giving context for the cycle diagram shown at right.</div>
    <div class="tx" style="margin-top:3px">One more short line adding a detail.</div>
  </div>
  <div class="block" style="left:0;top:71px;width:73px;height:37px"></div>
  <div class="abs" style="left:6px;top:74px;width:64px;color:#fff">
    <div style="font-size:3.6px;font-weight:600">● &nbsp;Lorem ipsum</div><div class="tx-w" style="margin:0 0 4px 7px">Short note on this point.</div>
    <div style="font-size:3.6px;font-weight:600">● &nbsp;Lorem ipsum</div><div class="tx-w" style="margin-left:7px">Short note on this point.</div>
  </div>
  <svg class="abs" style="left:82px;top:22px" width="140" height="94" viewBox="0 0 140 94" font-family="Poppins,sans-serif" font-size="3" fill="#1b1d3a">
    <path d="M90 18 A38 38 0 1 0 100 62" fill="none" stroke="#12187a" stroke-width="2.2"/>
    <path d="M20 42 l3 6 l3 -6" fill="none" stroke="#12187a" stroke-width="1.6"/>
    <circle cx="91" cy="16" r="9" fill="#2d45c8" stroke="#fff" stroke-width="1.5"/>
    <circle cx="100" cy="45" r="7" fill="#2d45c8" stroke="#fff" stroke-width="1.5"/>
    <circle cx="96" cy="72" r="7" fill="#12187a" stroke="#fff" stroke-width="1.5"/>
    <circle cx="46" cy="66" r="5" fill="#12187a" stroke="#fff" stroke-width="1.5"/>
    <rect x="37" y="30" width="2" height="6" fill="#12187a"/><rect x="40" y="27" width="2" height="9" fill="#12187a"/><rect x="43" y="31" width="2" height="5" fill="#12187a"/>
    <text x="34" y="42" font-weight="700" font-size="3.6">MAIN TITLE</text>
    <text x="103" y="8" font-weight="700" font-size="2.6">85%</text>
    <text x="115" y="14" font-weight="700" font-size="3">Your Title</text>
    <text x="82" y="40" font-weight="700" font-size="2.6">80%</text>
    <text x="116" y="44" font-weight="700" font-size="3">Your Title</text>
    <text x="55" y="64" font-weight="700" font-size="2.6">50%</text>
    <text x="22" y="62" font-weight="700" font-size="3">Your Title</text>
    <text x="107" y="82" font-weight="700" font-size="2.6">75%</text>
    <text x="116" y="72" font-weight="700" font-size="3">Your Title</text>
  </svg>
  <div class="foot"></div><div class="foot-mark">KV</div><div class="foot-url">www.website.com</div><div class="page">10</div>
</section>

<!-- Row 5 -->
<section class="slide" style="left:40px;top:606px">
  <div class="badge">KV</div>
  <div class="abs" style="left:8px;top:7px"><div class="title">Text Added Hare</div><span class="rule"></span></div>
  <div class="abs" style="left:15px;top:28px;width:97px">
    <div class="list-num">01. <span style="color:var(--royal)">Text Added Here</span></div><div class="tx" style="margin-bottom:5px">A short paragraph for the first point with a few plain words that fill two lines.</div>
    <div class="list-num">02. <span style="color:var(--royal)">Text Added Here</span></div><div class="tx" style="margin-bottom:5px">A short paragraph for the second point with a few plain words that fill two lines.</div>
    <div class="list-num">03. <span style="color:var(--royal)">Text Added Here</span></div><div class="tx">A short paragraph for the third point with a few plain words that fill two lines.</div>
  </div>
  <div class="block" style="left:125px;top:22px;width:72px;height:8px"></div>
  <div class="photo" role="img" aria-label="Photo of two businessmen reviewing a tablet" style="left:132px;top:30px;width:72px;height:76px"></div>
  <div class="foot"></div><div class="foot-mark">KV</div><div class="foot-url">www.website.com</div><div class="page">11</div>
</section>

<section class="slide" style="left:282px;top:606px">
  <div class="badge">KV</div>
  <div class="abs" style="left:8px;top:7px"><div class="title">Text Added Hare</div><span class="rule"></span></div>
  <div class="abs" style="left:15px;top:27px;width:96px">
    <div class="list-num">01. <span style="color:var(--royal)">Text Added Here</span></div>
    <div class="tx" style="margin-bottom:3px">A short paragraph for this section with a few plain words that fill the lines.</div>
    <div class="tx" style="margin-bottom:5px">One more short line to add detail to the point.</div>
    <div class="list-num">02. <span style="color:var(--royal)">Text Added Here</span></div>
    <div class="tx" style="margin-bottom:3px">A short paragraph for this section with a few plain words that fill the lines.</div>
    <div class="tx">One more short line to add detail to the point.</div>
  </div>
  <div class="abs" style="left:123px;top:34px;font-size:4.4px;line-height:2.8;font-weight:500">
    <div>• Fits Your Business Or Products</div><div>• Is Easy To Spell And Remember</div><div>• Fits Your Business Or Products</div><div>• Is Easy To Spell And Remember</div><div>• Fits Your Business Or Products</div><div>• Is Easy To Spell And Remember</div>
  </div>
  <div class="foot"></div><div class="foot-mark">KV</div><div class="foot-url">www.website.com</div><div class="page">12</div>
</section>

<section class="slide" style="left:523px;top:606px">
  <div class="badge">KV</div>
  <div class="abs" style="left:8px;top:7px"><div class="title">Text Added Hare</div><span class="rule"></span></div>
  <div class="abs" style="left:15px;top:28px;width:97px">
    <div style="font-size:5.6px;font-weight:500;color:var(--royal)">01. <span style="color:var(--ink)">Text Added Here</span></div>
    <div class="tx" style="margin:2px 0 3px">A short paragraph of body copy for the first column that runs across a few plain lines of text.</div>
    <div class="tx" style="margin-bottom:3px">Another short paragraph of body copy for this column with a few more plain words here.</div>
    <div class="tx">A closing line of copy for this column.</div>
  </div>
  <div class="abs" style="left:119px;top:28px;width:97px">
    <div style="font-size:5.6px;font-weight:500;color:var(--royal)">02. <span style="color:var(--ink)">Text Added Here</span></div>
    <div class="tx" style="margin:2px 0 3px">A short paragraph of body copy for the second column that runs across a few plain lines of text.</div>
    <div class="tx" style="margin-bottom:3px">Another short paragraph of body copy for this column with a few more plain words here.</div>
    <div class="tx">A closing line of copy for this column.</div>
  </div>
  <div class="foot"></div><div class="foot-mark">KV</div><div class="foot-url">www.website.com</div><div class="page">13</div>
</section>

<!-- Row 6 -->
<section class="slide" style="left:40px;top:748px">
  <div class="badge">KV</div>
  <div class="block" style="left:0;top:0;width:37px;height:72px"></div>
  <div class="photo-warm" role="img" aria-label="Photo of stacked books with a graduation cap and diploma" style="left:13px;top:16px;width:79px;height:94px"></div>
  <div class="block" style="left:38px;top:96px;width:38px;height:11px;display:flex;align-items:center;justify-content:center;color:#fff;font-size:6.5px;font-weight:600">Service</div>
  <div class="abs" style="left:225px;top:36px;width:3px;height:48px;background:var(--navy)"></div>
  <div class="abs" style="left:104px;top:27px;width:112px">
    <div style="display:flex;gap:8px;margin-bottom:11px"><span class="icon-dot" style="position:static;flex:none"></span><div><div class="sub">Project name</div><div class="tx">Short note for this project item here.</div></div></div>
    <div style="display:flex;gap:8px;margin-bottom:11px"><span class="icon-dot" style="position:static;flex:none"></span><div><div class="sub">Project name</div><div class="tx">Short note for this project item here.</div></div></div>
    <div style="display:flex;gap:8px"><span class="icon-dot" style="position:static;flex:none"></span><div><div class="sub">Project name</div><div class="tx">Short note for this project item here.</div></div></div>
  </div>
  <div class="foot"></div><div class="foot-mark">KV</div><div class="foot-url">www.website.com</div><div class="page">14</div>
</section>

<section class="slide" style="left:282px;top:748px">
  <div class="badge">KV</div>
  <div class="abs" style="left:8px;top:7px"><div class="title">Text Added Hare</div><span class="rule"></span></div>
  <div class="abs" style="left:225px;top:32px;width:3px;height:74px;background:var(--navy)"></div>
  <svg class="abs" style="left:40px;top:22px" width="170" height="100" viewBox="0 0 170 100" font-family="Poppins,sans-serif" text-anchor="middle">
    <line x1="73" y1="2" x2="73" y2="98" stroke="#9aa0c4" stroke-width=".6" stroke-dasharray="1 1.5"/>
    <line x1="25" y1="50" x2="121" y2="50" stroke="#9aa0c4" stroke-width=".6" stroke-dasharray="1 1.5"/>
    <circle cx="54" cy="31" r="16" fill="#2233b0"/><circle cx="92" cy="31" r="16" fill="#12187a"/>
    <circle cx="54" cy="69" r="16" fill="#12187a"/><circle cx="92" cy="69" r="16" fill="#2233b0"/>
    <circle cx="73" cy="50" r="12" fill="#0c1060" stroke="#fff" stroke-width="1.2"/>
    <g fill="#fff" font-weight="600" font-size="14"><text x="54" y="36">S</text><text x="92" y="36">W</text><text x="54" y="74">O</text><text x="92" y="74">T</text></g>
    <text x="73" y="51.5" fill="#fff" font-size="3.6" font-style="italic">ANALYSIS</text>
    <g font-size="3.2" font-weight="600" font-style="italic" fill="#12187a"><text x="17" y="9">STRENGTHS</text><text x="128" y="8">WEAKNESSES</text><text x="16" y="67">OPPORTUNITIES</text><text x="124" y="74">THREATS</text></g>
    <g font-size="2" fill="#8c90a8" text-anchor="start"><text x="8" y="13">• Good location</text><text x="8" y="17">• Fair prices</text><text x="8" y="21">• Many options</text><text x="115" y="12">• Few promotions</text><text x="115" y="25">• Small team</text><text x="8" y="71">• Hire more staff</text><text x="8" y="79">• New app idea</text><text x="115" y="78">• New gyms nearby</text><text x="115" y="88">• Price pressure</text></g>
  </svg>
  <div class="foot"></div><div class="foot-mark">KV</div><div class="foot-url">www.website.com</div><div class="page">15</div>
</section>

<section class="slide" style="left:523px;top:748px">
  <div class="badge">KV</div>
  <div class="abs" style="left:8px;top:7px"><div class="title">Text Added Hare</div><span class="rule"></span></div>
  <div class="abs" style="left:22px;top:39px;width:56px;height:56px;border-radius:50%;border:1.4px solid var(--navy);padding:3px"><div style="width:100%;height:100%;border-radius:50%;background:var(--grad);color:#fff;font-size:8px;font-weight:700;line-height:1.1;display:flex;align-items:center;justify-content:center;text-align:center">Text<br>Added<br>Hare</div></div>
  <svg class="abs" style="left:78px;top:34px" width="36" height="66" viewBox="0 0 36 66"><path d="M2 20 L14 2 L34 2 M3 33 L34 33 M2 46 L14 64 L34 64" fill="none" stroke="#555" stroke-width=".4"/></svg>
  <div class="abs" style="left:113px;top:29px;width:104px">
    <div style="display:flex;gap:10px;margin-bottom:12px"><span class="icon-dot" style="position:static;flex:none"></span><div><div class="sub">Project name</div><div class="tx">Short note for this project item here.</div></div></div>
    <div style="display:flex;gap:10px;margin-bottom:12px"><span class="icon-dot" style="position:static;flex:none"></span><div><div class="sub">Project name</div><div class="tx">Short note for this project item here.</div></div></div>
    <div style="display:flex;gap:10px"><span class="icon-dot" style="position:static;flex:none"></span><div><div class="sub">Project name</div><div class="tx">Short note for this project item here.</div></div></div>
  </div>
  <div class="foot"></div><div class="foot-mark">KV</div><div class="foot-url">www.website.com</div><div class="page">16</div>
</section>

<!-- Row 7 -->
<section class="slide" style="left:40px;top:890px">
  <div class="badge">KV</div>
  <div class="block" style="left:0;top:9px;width:119px;height:12px;display:flex;align-items:center;padding-left:11px;color:#fff;font-size:8px;font-weight:700">Project Timeline - 2024</div>
  <svg class="abs" style="left:0;top:36px" width="228" height="80" viewBox="0 0 228 80" font-family="Poppins,sans-serif" text-anchor="middle">
    <g fill="#12187a"><polygon points="22,30 55,30 52,36 18,36"/><polygon points="58,30 92,30 88,36 54,36" fill="#2233b0"/><polygon points="94,30 128,30 124,36 90,36"/><polygon points="131,30 165,30 161,36 127,36" fill="#2233b0"/><polygon points="167,30 201,30 197,36 163,36"/></g>
    <g fill="#fff" font-size="3.2" font-weight="600"><text x="37" y="34.5">1990</text><text x="73" y="34.5">2001</text><text x="109" y="34.5">2007</text><text x="146" y="34.5">2012</text><text x="182" y="34.5">2020</text></g>
    <g stroke="#12187a" stroke-width=".6"><line x1="37" y1="18" x2="37" y2="28"/><line x1="109" y1="18" x2="109" y2="28"/><line x1="182" y1="18" x2="182" y2="28"/><line x1="73" y1="38" x2="73" y2="47"/><line x1="146" y1="38" x2="146" y2="47"/></g>
    <g fill="#12187a"><circle cx="37" cy="19" r="1"/><circle cx="109" cy="19" r="1"/><circle cx="182" cy="19" r="1"/><circle cx="73" cy="47" r="1"/><circle cx="146" cy="47" r="1"/></g>
    <g font-size="3.6" font-weight="600" fill="#2233b0"><text x="37" y="5">Your Title</text><text x="109" y="5">Your Title</text><text x="182" y="5">Your Title</text><text x="73" y="56">Your Title</text><text x="146" y="56">Your Title</text></g>
    <g font-size="2.5" fill="#8c90a8"><text x="37" y="9">Refers to a good or</text><text x="37" y="12">service being offered</text><text x="109" y="9">Refers to a good or</text><text x="109" y="12">service being offered</text><text x="182" y="9">Refers to a good or</text><text x="182" y="12">service being offered</text><text x="73" y="60">Refers to a good or</text><text x="73" y="63">service being offered</text><text x="146" y="60">Refers to a good or</text><text x="146" y="63">service being offered</text></g>
  </svg>
  <div class="foot"></div><div class="foot-mark">KV</div><div class="foot-url">www.website.com</div><div class="page">17</div>
</section>

<section class="slide" style="left:282px;top:890px">
  <div class="badge">KV</div>
  <div class="block" style="left:0;top:17px;width:90px;height:94px"></div>
  <div class="abs" style="left:25px;top:64px;transform:translate(-50%,-50%) rotate(90deg);color:#fff;font-size:6px;font-weight:600;letter-spacing:2px;white-space:nowrap">TEXT ADDED</div>
  <div class="abs" style="left:50px;top:29px;width:58px;display:flex;flex-direction:column;gap:9px">
    <div style="background:var(--royal);color:#fff;font-size:5px;font-weight:600;padding:4px 7px;box-shadow:1px 1px 2px rgba(0,0,0,.3)">1. Lorem Ipsum</div>
    <div style="background:var(--royal);color:#fff;font-size:5px;font-weight:600;padding:4px 7px;box-shadow:1px 1px 2px rgba(0,0,0,.3)">2. Lorem Ipsum</div>
    <div style="background:var(--royal);color:#fff;font-size:5px;font-weight:600;padding:4px 7px;box-shadow:1px 1px 2px rgba(0,0,0,.3)">3. Lorem Ipsum</div>
  </div>
  <div class="abs" style="left:119px;top:30px;width:90px">
    <div class="title" style="font-size:9.5px;color:var(--ink);line-height:1.25">Text<br>Added Hare</div>
    <div style="font-size:3.2px;line-height:1.4;color:#555;margin-top:9px">A short line of body copy for this slide here.</div>
    <div style="font-size:3.2px;line-height:1.4;color:#555;margin-top:4px">A second short paragraph of body copy that runs over a few lines to balance the layout well.</div>
  </div>
  <div class="foot"></div><div class="foot-mark">KV</div><div class="foot-url">www.website.com</div><div class="page">18</div>
</section>

<section class="slide" style="left:523px;top:890px">
  <div class="badge">KV</div>
  <div class="abs" style="left:8px;top:7px"><div class="title">Text Added Hare</div><span class="rule"></span></div>
  <svg class="abs" style="left:12px;top:34px" width="206" height="60" viewBox="0 0 206 60" font-family="Poppins,sans-serif" text-anchor="middle">
    <rect x="2" y="27" width="196" height="3" fill="#12187a"/><polygon points="196,24.5 204,28.5 196,32.5" fill="#2233b0"/>
    <g fill="#fff" stroke="#12187a" stroke-width="2.4"><circle cx="40" cy="13" r="10"/><circle cx="80" cy="13" r="10"/><circle cx="120" cy="13" r="10"/><circle cx="160" cy="13" r="10"/></g>
    <g fill="none" stroke="#12187a" stroke-width=".9"><circle cx="40" cy="13" r="4"/><path d="M40 11v2.5l1.5 1"/><circle cx="120" cy="13" r="4"/><circle cx="161" cy="12" r="3"/><path d="M159 14l-3 3"/></g>
    <circle cx="80" cy="14" r="4" fill="#12187a"/>
    <g fill="#fff" font-size="2.6"><text x="40" y="29.3">Step 01</text><text x="80" y="29.3">Step 02</text><text x="120" y="29.3">Step 03</text><text x="160" y="29.3">Step 04</text></g>
    <g stroke="#555" stroke-width=".4"><line x1="40" y1="31" x2="40" y2="37"/><line x1="80" y1="31" x2="80" y2="37"/><line x1="120" y1="31" x2="120" y2="37"/><line x1="160" y1="31" x2="160" y2="37"/></g>
    <g font-size="4" font-weight="500" fill="#1b1d3a"><text x="40" y="43">Lorem Ipsum</text><text x="80" y="43">Lorem Ipsum</text><text x="120" y="43">Lorem Ipsum</text><text x="160" y="43">Lorem Ipsum</text></g>
    <g font-size="2.2" fill="#8c90a8"><text x="40" y="47">Short note for step one.</text><text x="80" y="47">Short note for step two.</text><text x="120" y="47">Short note for step three.</text><text x="160" y="47">Short note for step four.</text></g>
  </svg>
  <div class="foot"></div><div class="foot-mark">KV</div><div class="foot-url">www.website.com</div><div class="page">19</div>
</section>

<!-- Row 8 -->
<section class="slide" style="left:40px;top:1033px">
  <div class="badge">KV</div>
  <div class="abs" style="left:15px;top:13px;font-weight:700;font-size:11.5px;line-height:1.15;color:var(--royal)">Text<br>Added<br>Here</div>
  <div class="abs" style="left:88px;top:30px;width:115px;height:75px;background:radial-gradient(ellipse at center,#eef0f5,#fff 70%)" role="img" aria-label="Faint world map backdrop"></div>
  <div class="block" style="left:0;top:57px;width:85px;height:50px"></div>
  <div class="abs" style="left:13px;top:61px;width:70px;color:#fff">
    <div style="display:flex;gap:4px;margin-bottom:4px"><span style="background:#fff;color:var(--navy);font-size:4px;font-weight:700;padding:0 2px;height:6px">1.</span><div><div style="font-size:3.4px;font-weight:600">Lorem ipsum</div><div class="tx-w">Short note on this item.</div></div></div>
    <div style="display:flex;gap:4px;margin-bottom:4px"><span style="background:#fff;color:var(--navy);font-size:4px;font-weight:700;padding:0 2px;height:6px">2.</span><div><div style="font-size:3.4px;font-weight:600">Lorem ipsum</div><div class="tx-w">Short note on this item.</div></div></div>
    <div style="display:flex;gap:4px"><span style="background:#fff;color:var(--navy);font-size:4px;font-weight:700;padding:0 2px;height:6px">3.</span><div><div style="font-size:3.4px;font-weight:600">Lorem ipsum</div><div class="tx-w">Short note on this item.</div></div></div>
  </div>
  <div class="abs" style="left:102px;top:21px;width:27px;height:54px;border:1px solid #333;border-radius:3px;background:#fff;padding:6px 3px">
    <div style="font-size:3px;font-weight:600">Lorem ipsum dolor</div><div style="width:8px;height:5px;border:.5px solid var(--navy);margin:5px auto"></div><div class="tx" style="font-size:1.8px">Short note on this screen here.</div></div>
  <div class="abs" style="left:138px;top:38px;width:27px;height:54px;border:1px solid #333;border-radius:3px;background:#fff;padding:6px 3px">
    <div style="font-size:3px;font-weight:600">Dolor sit amet, conse</div><div style="width:7px;height:7px;border:.5px solid var(--navy);border-radius:50%;margin:5px auto"></div><div class="tx" style="font-size:1.8px">Short note on this screen here.</div></div>
  <div class="abs" style="left:172px;top:58px;width:27px;height:56px;border:1px solid #333;border-radius:3px;background:#fff;padding:6px 3px">
    <div style="font-size:3px;font-weight:600">Consec</div><div style="width:7px;height:7px;border:.5px solid var(--navy);margin:5px auto"></div><div class="tx" style="font-size:1.8px">Short note on this screen here.</div></div>
  <div class="foot"></div><div class="foot-mark">KV</div><div class="foot-url">www.website.com</div><div class="page">20</div>
</section>

<section class="slide" style="left:282px;top:1033px">
  <div class="badge">KV</div>
  <div class="block" style="left:15px;top:26px;width:198px;height:31px;display:flex;justify-content:center;padding-top:5px;color:#fff;font-size:7.5px;font-weight:700">The Team Members</div>
  <div class="abs" style="left:20px;top:44px;width:188px;display:flex;justify-content:space-between">
    <div class="member"><div class="member-photo" role="img" aria-label="Portrait of team member Owen Hale"></div><div class="member-name">OWEN HALE</div><div class="tx">Short bio line for this team member here.</div></div>
    <div class="member"><div class="member-photo" role="img" aria-label="Portrait of team member Nora Vance"></div><div class="member-name">NORA VANCE</div><div class="tx">Short bio line for this team member here.</div></div>
    <div class="member"><div class="member-photo" role="img" aria-label="Portrait of team member Owen Hale"></div><div class="member-name">OWEN HALE</div><div class="tx">Short bio line for this team member here.</div></div>
    <div class="member"><div class="member-photo" role="img" aria-label="Portrait of team member Nora Vance"></div><div class="member-name">NORA VANCE</div><div class="tx">Short bio line for this team member here.</div></div>
  </div>
  <div class="foot"></div><div class="foot-mark">KV</div><div class="foot-url">www.website.com</div><div class="page">21</div>
</section>

<section class="slide" style="left:523px;top:1033px">
  <div class="abs" style="left:8px;top:24px;font-size:54px;font-weight:700;color:var(--navy);line-height:1">KV</div>
  <div class="abs" style="left:132px;top:38px">
    <div style="font-family:'Oswald',sans-serif;font-weight:600;font-size:15px;color:var(--ink);line-height:1">Thank You</div>
    <div style="margin-top:8px;display:flex;flex-direction:column;gap:6px;font-size:3.4px;color:#444;line-height:1.35">
      <div style="display:flex;gap:5px;align-items:center"><svg width="6" height="6" viewBox="0 0 24 24"><path fill="#2233b0" d="M6.6 10.8a15 15 0 006.6 6.6l2.2-2.2c.3-.3.7-.4 1-.2 1.1.4 2.3.6 3.6.6.6 0 1 .4 1 1V20c0 .6-.4 1-1 1A17 17 0 013 4c0-.6.4-1 1-1h3.5c.6 0 1 .4 1 1 0 1.3.2 2.5.6 3.6.1.3 0 .7-.2 1z"/></svg><span style="border-left:.5px solid #444;padding-left:3px">+10 5550 3142 7781<br>+10 5550 3142 7782</span></div>
      <div style="display:flex;gap:5px;align-items:center"><svg width="6" height="6" viewBox="0 0 24 24"><path fill="#2233b0" d="M2 12l20-9-9 20-2-9z"/></svg><span style="border-left:.5px solid #444;padding-left:3px">www.websitename.com<br>urname@email.com</span></div>
      <div style="display:flex;gap:5px;align-items:center"><svg width="6" height="6" viewBox="0 0 24 24"><path fill="#2233b0" d="M12 3l10 9h-3v9h-5v-6h-4v6H5v-9H2z"/></svg><span style="border-left:.5px solid #444;padding-left:3px">1234 Street name, town/city,<br>state/country, post/zip 012345.</span></div>
    </div>
  </div>
</section>

</body>
</html>
```